Business Card Design for Varnok Facility Services

We are looking for a Business Card Design for the Company "Varnok Facility Services."
Front side:
- Company Logo (small)
- Company Name, address, pohone, website and personal data.
- white background, for text e.g. company colors (blue or green like in the logo)
Please use following data:
Company data:
Varnok Facility Services Tulbrecht
Kirchmattweg 12
6331 Cham
www.varnok-fs.ch
Person data:
Ruben Tulbrecht
Geschäftsführer
+41 76 519 84 60
info@varnok-fs.ch
Back side:
could be colored in blue or green
please use a big logo sing and some smaller icons to say what is all beeing offered in facility services, like cleaning, maintenance cleaning
industrial cleaning, caretaking, gardening, disposal. There is no need for everyone of the icons if there are similar or an icon is standing for more of them.
Cleaning Service
colors to use:
blue: HEX 246BB0
green: HEX 52B33E

```html
<!DOCTYPE html>
<html lang="de">
<head>
<meta charset="utf-8">
<title>Varnok Facility Services – Visitenkarte</title>
<link rel="stylesheet" href="https://fonts.googleapis.com/css2?family=Open+Sans:wght@400;600;700&display=swap">
<style>
  :root {
    --brand-blue: #246BB0;
    --brand-green: #52B33E;
    --ink: #1d1d1d;
    --paper: #ffffff;
    --backdrop: #f1f1f1;
    --edge: #d6d6d6;
  }
  * { box-sizing: border-box; margin: 0; padding: 0; }
  html, body {
    width: 867px; height: 1200px; overflow: hidden;
    background: var(--backdrop);
    font-family: "Open Sans", Arial, sans-serif;
  }
  .canvas { position: relative; width: 867px; height: 1200px; }

  .card {
    position: absolute; left: 0; width: 867px;
    background: var(--paper);
    border: 1px solid var(--edge);
  }
  .card--front { top: 0; height: 615px; }
  .card--back { top: 659px; height: 541px; }

  .brand {
    position: absolute;
    display: flex; align-items: center; gap: 18px;
    color: var(--brand-blue); font-weight: 700;
  }
  .brand__dot {
    flex: none; border-radius: 50%; background: var(--brand-green);
  }
  .brand__name { line-height: 1.1; }

  .card--front .brand { left: 0; right: 0; top: 100px; justify-content: center; }
  .card--front .brand__dot { width: 46px; height: 46px; }
  .card--front .brand__name { font-size: 44px; }

  .company-box {
    position: absolute; left: 35px; top: 312px; width: 451px; height: 150px;
    background: var(--brand-green); color: var(--paper);
    padding: 22px 26px; font-size: 21px; line-height: 1.32;
  }
  .company-box__name { font-weight: 700; }

  .person {
    position: absolute; left: 512px; top: 320px;
    color: var(--ink); font-size: 21px; line-height: 1.32;
  }
  .person__name { font-weight: 700; }

  .accent-square {
    position: absolute; left: 728px; top: 312px; width: 104px; height: 150px;
    background: var(--brand-blue);
  }

  .card--back .brand {
    left: 60px; top: 905px; top: 246px; width: 350px;
  }
  .card--back .brand__dot { width: 40px; height: 40px; }
  .card--back .brand__name { font-size: 30px; }

  .services {
    position: absolute; left: 433px; top: 35px; width: 399px; height: 468px;
    background: var(--brand-blue); color: var(--paper);
    padding: 160px 0 0 52px;
  }
  .services__list { list-style: none; font-size: 24px; line-height: 1; }
  .services__item { display: flex; align-items: center; gap: 16px; margin-bottom: 21px; }
  .services__item::before {
    content: ""; width: 8px; height: 8px; border-radius: 50%; background: var(--paper);
  }
</style>
</head>
<body>
<main class="canvas">
  <section class="card card--front" aria-label="Vorderseite">
    <div class="brand">
      <span class="brand__dot"></span>
      <span class="brand__name">Varnok Facility Services</span>
    </div>
    <div class="company-box">
      <p class="company-box__name">Varnok Facility Services Tulbrecht</p>
      <p>Kirchmattweg 12</p>
      <p>6331 Cham</p>
      <p>www.varnok-fs.ch</p>
    </div>
    <div class="person">
      <p class="person__name">Ruben Tulbrecht</p>
      <p>Geschäftsführer</p>
      <p>+41 76 519 84 60</p>
      <p>info@varnok-fs.ch</p>
    </div>
    <div class="accent-square"></div>
  </section>

  <section class="card card--back" aria-label="Rückseite">
    <div class="brand">
      <span class="brand__dot"></span>
      <span class="brand__name">Varnok Facility Services</span>
    </div>
    <div class="services">
      <ul class="services__list">
        <li class="services__item">Cleaning</li>
        <li class="services__item">Maintenance Cleaning</li>
        <li class="services__item">Industrial Cleaning</li>
        <li class="services__item">Caretaking</li>
        <li class="services__item">Gardening</li>
        <li class="services__item">Disposal</li>
      </ul>
    </div>
  </section>
</main>
</body>
</html>
```